Black Granite Web Design Project

We are looking for a design for a new company that will be selling Black Granite slabs and tiles. We will be selling to both end-consumers and granite installers. We have already settled on a logo and hopefully this will give an idea of what we like in our designs. We are not going to be selling online but want people to call us so the site is basically an enhanced business card. We will be focusing a lot on SEO so the design will have to keep that in mind.

We would like to keep the design in 1024x768 to make it easily view-able on all devices.

Regarding navigation there should only be a few sub-pages, like "Granite Slabs", "Granite Tiles", "Delivery", "Contact"

Aside from that we are open to designs. One idea we did have was to personalize the site and have a person there somehow to represent the company, making the user feel there are real people behind this site. This is just an idea and not a must.

The name of the company and site is "Silver Brook Petrano"

Thanks
Updates

Hello All,

Thanks for the great designs. There are some good looking designs that show beautiful kitchens but this site is made for the granite installers and not the retail consumers. So in order not to to confuse the buyers I would like to keep this as much about the raw products as possible. The raw products being the granite slabs, thereby making it obvious we don't sell granite counter tops. 

This design will really be the identity of this company so it is important we get the right message across on this index page and that this page is as complete as possible.

Again, thanks for all the work being put into this.

Target Market(s)

The target audience is granite installers or companies that would with granite slabs.

Industry/Entity Type

Business

```html
<!DOCTYPE html>
<html lang="en">
<head>
<meta charset="utf-8">
<title>Silver Brook Petrano – Granite Slabs &amp; Tiles</title>
<link rel="stylesheet" href="https://fonts.googleapis.com/css2?family=Open+Sans:wght@400;600;700;800&display=swap">
<style>
  :root {
    --page-bg: #e8e8e6;
    --panel: #ffffff;
    --ink: #2b2b2b;
    --muted: #6d6d6d;
    --line: #d2d2d0;
    --dark: #1f1f1f;
    --nav: #262626;
    --sky: #9fb7cf;
  }
  * { box-sizing: border-box; margin: 0; padding: 0; }
  html, body { width: 800px; height: 1200px; overflow: hidden; }
  body {
    background: var(--page-bg);
    font-family: "Open Sans", Arial, sans-serif;
    color: var(--ink);
    position: relative;
  }
  .abs { position: absolute; }

  /* top bar */
  .topbar { left: 80px; top: 6px; font-size: 9px; color: var(--muted); letter-spacing: .2px; }

  /* header */
  .brand { left: 80px; top: 34px; display: flex; align-items: center; gap: 10px; }
  .brand-square { width: 38px; height: 38px; background: var(--dark); }
  .brand-name { font-size: 15px; font-weight: 800; color: var(--dark); line-height: 1; letter-spacing: .3px; }
  .brand-place { font-size: 8px; font-weight: 600; color: var(--muted); letter-spacing: 1.5px; margin-top: 4px; }
  .main-nav { left: 356px; top: 44px; width: 364px; height: 30px; background: var(--nav);
    display: flex; justify-content: space-between; align-items: center; padding: 0 10px; }
  .main-nav a { color: #fff; text-decoration: none; font-size: 8px; font-weight: 700; letter-spacing: .2px; white-space: nowrap; }

  /* hero */
  .hero { left: 80px; top: 108px; width: 640px; height: 256px; overflow: hidden;
    background: linear-gradient(180deg, var(--sky) 0%, #c9d3d8 30%, #a8a49a 55%, #7d7a72 100%); }
  .hero-caption { position: absolute; left: 0; top: 172px; width: 400px; padding: 8px 14px;
    background: rgba(20,20,20,.72); color: #fff; font-size: 17px; font-weight: 800; line-height: 1.2; }
  .hero-quote { position: absolute; left: 400px; top: 12px; width: 220px; padding: 7px 9px;
    background: rgba(255,255,255,.92); font-size: 8px; line-height: 1.35; color: var(--ink); }
  .hero-quote-name { display: inline-block; margin-top: 4px; background: var(--dark); color: #fff;
    font-size: 8px; font-weight: 700; padding: 2px 8px; }
  .hero-arrow { position: absolute; top: 112px; width: 22px; height: 22px; border-radius: 50%;
    background: rgba(255,255,255,.85); }
  .hero-arrow svg { display: block; }
  .hero-dots { left: 380px; top: 372px; display: flex; gap: 6px; }
  .hero-dots span { width: 7px; height: 7px; border-radius: 50%; background: #b5b5b3; }
  .hero-dots span.is-active { background: var(--dark); }

  /* welcome */
  .welcome { left: 80px; top: 388px; width: 640px; height: 58px; background: var(--panel); padding: 9px 12px; }
  .welcome h1 { font-size: 14px; font-weight: 600; color: var(--dark); letter-spacing: .3px; }
  .welcome p { font-size: 8.5px; color: var(--muted); width: 520px; margin-top: 4px; line-height: 1.35; text-transform: uppercase; }
  .welcome-seal { position: absolute; right: 12px; top: -6px; width: 58px; height: 58px; border-radius: 50%;
    background: var(--dark); border: 3px solid #fff; box-shadow: 0 0 0 1px var(--line); }

  /* features */
  .features { left: 80px; top: 460px; width: 640px; display: flex; gap: 10px; }
  .feature { flex: 1; height: 140px; background: var(--panel); border: 1px solid var(--line); text-align: center; padding-top: 12px; }
  .feature h2 { font-size: 10px; font-weight: 600; letter-spacing: .5px; color: var(--dark); }
  .feature svg { display: block; margin: 8px auto 8px; }
  .feature p { font-size: 8px; color: var(--muted); line-height: 1.35; width: 150px; margin: 0 auto; text-align: left; }
  .feature .more { display: block; font-weight: 700; color: var(--ink); }

  /* section titles */
  .section-title { font-size: 9px; font-weight: 700; color: var(--dark); letter-spacing: .5px; text-align: center; }

  /* products */
  .products { left: 80px; top: 628px; width: 640px; display: flex; gap: 22px; }
  .product { flex: 1; text-align: center; }
  .product-photo { height: 132px; }
  .product h3 { font-size: 9.5px; font-weight: 700; margin-top: 10px; color: var(--dark); }
  .product p { font-size: 7.5px; color: var(--muted); margin-top: 3px; line-height: 1.3; padding: 0 20px; }
  .photo-prefab { background: radial-gradient(circle at 40% 40%, #c9a58c, #8c6a55 60%, #5f4636); }
  .photo-raw { background: linear-gradient(135deg, #e8dccb, #c8b49a 50%, #a88f73); }
  .photo-tiles { background: linear-gradient(135deg, #b98c7c, #8fa0b4 40%, #c6b9a4 70%, #6f6a66); }

  /* gallery */
  .gallery-head { left: 80px; top: 846px; width: 640px; height: 18px; border-bottom: 1px solid var(--line); }
  .gallery-arrows { position: absolute; right: 0; top: 0; display: flex; gap: 2px; }
  .gallery-arrows span { width: 14px; height: 14px; background: var(--dark); display: flex; align-items: center; justify-content: center; }
  .gallery { left: 80px; top: 868px; width: 640px; height: 132px; display: flex; gap: 4px; }
  .gallery div { flex: 1; }
  .g1 { background: linear-gradient(160deg, #7d4a3c, #a9705a 50%, #5e3a30); }
  .g2 { background: linear-gradient(160deg, #cdbfa9, #a99880 50%, #d6cbbb); }
  .g3 { background: linear-gradient(160deg, #a47c5c, #c7a27c 50%, #7f5e44); }
  .g4 { background: linear-gradient(160deg, #5d5d5d, #8a8a88 50%, #4a4a4a); }
  .g5 { background: linear-gradient(160deg, #d9d6cf, #b3afa6 50%, #ecebe6); }
  .g6 { background: linear-gradient(160deg, #b9a08c, #d7c4b1 50%, #9a8471); }

  /* footer */
  .footer { left: 80px; top: 1026px; width: 640px; height: 142px; border-top: 1px solid var(--line); padding-top: 8px; }
  .footer-col { position: absolute; top: 8px; }
  .footer-col h4 { font-size: 8.5px; font-weight: 700; color: var(--dark); padding-bottom: 4px; border-bottom: 1px solid var(--line); width: 110px; margin-bottom: 4px; }
  .footer-col li { list-style: none; font-size: 8px; color: var(--muted); line-height: 1.55; }
  .footer-call { position: absolute; right: 0; top: 10px; text-align: right; }
  .footer-call .phone { font-size: 16px; font-weight: 800; color: var(--dark); }
  .footer-brand { display: flex; align-items: center; gap: 8px; justify-content: flex-end; margin-top: 12px; }
  .footer-brand .brand-square { width: 28px; height: 28px; }
  .footer-brand .brand-name { font-size: 11px; }
  .footer-call address { font-style: normal; font-size: 7.5px; color: var(--muted); line-height: 1.4; margin-top: 8px; width: 140px; margin-left: auto; }
  .copyright { left: 80px; top: 1172px; font-size: 7.5px; color: var(--muted); line-height: 1.35; }
</style>
</head>
<body>

  <div class="abs topbar">Email: info@silverbrookpetrano.com &nbsp;|&nbsp; CALL: (555) 284-7730</div>

  <header>
    <div class="abs brand">
      <span class="brand-square"></span>
      <div>
        <div class="brand-name">SILVER BROOK PETRANO</div>
        <div class="brand-place">PORTO VERDE</div>
      </div>
    </div>
    <nav class="abs main-nav">
      <a href="#">HOME</a><a href="#">ABOUT US</a><a href="#">GRANITE TILES</a>
      <a href="#">GRANITE SLABS</a><a href="#">DELIVERY</a><a href="#">CONTACT US</a>
    </nav>
  </header>

  <section class="abs hero" role="img" aria-label="Granite slabs stacked in a quarry yard with a company representative standing on the right">
    <div class="hero-quote">Meet our team in person. We help you choose the right slab for every job.<br>
      <span class="hero-quote-name">Sales Manager</span></div>
    <div class="hero-caption">PROFESSIONALLY CUT, HIGH QUALITY<br>GRANITE SLABS FOR YOUR DREAM HOMES</div>
    <span class="hero-arrow" style="left:10px"><svg width="22" height="22"><path d="M13 6 L8 11 L13 16" fill="none" stroke="#222" stroke-width="2"/></svg></span>
    <span class="hero-arrow" style="left:608px"><svg width="22" height="22"><path d="M9 6 L14 11 L9 16" fill="none" stroke="#222" stroke-width="2"/></svg></span>
  </section>
  <div class="abs hero-dots"><span class="is-active"></span><span></span><span></span></div>

  <section class="abs welcome">
    <h1>WELCOME TO SILVER BROOK PETRANO</h1>
    <p>We supply raw granite slabs and tiles cut to exact size for installers and stone companies. Every block is selected at the quarry and finished in our own workshop before delivery.</p>
    <span class="welcome-seal"></span>
  </section>

  <section class="abs features">
    <article class="feature">
      <h2>PREMIUM QUALITY</h2>
      <svg width="34" height="34" viewBox="0 0 34 34"><rect x="3" y="3" width="28" height="28" fill="none" stroke="#222" stroke-width="3"/><path d="M9 17 L15 23 L25 11" fill="none" stroke="#222" stroke-width="3"/></svg>
      <p>Every slab is checked for colour, veining and thickness before it leaves our yard. <span class="more">Read more...</span></p>
    </article>
    <article class="feature">
      <h2>PERFECT CUT</h2>
      <svg width="34" height="34" viewBox="0 0 34 34"><path d="M4 12 H24 M18 6 L25 12 L18 18" fill="none" stroke="#222" stroke-width="3"/><path d="M30 24 H10 M16 18 L9 24 L16 30" fill="none" stroke="#222" stroke-width="3"/></svg>
      <p>Blocks are cut on modern gang saws to exact, even thickness for easy fitting. <span class="more">Read more...</span></p>
    </article>
    <article class="feature">
      <h2>EXCELLENT SERVICE</h2>
      <svg width="34" height="34" viewBox="0 0 34 34"><circle cx="17" cy="13" r="10" fill="#222"/><path d="M10 21 L7 32 L13 29 L17 32 L21 29 L27 32 L24 21" fill="#222"/><path d="M12 13 L16 17 L22 9" fill="none" stroke="#fff" stroke-width="2.5"/></svg>
      <p>Our team answers calls fast and plans every delivery around your site. <span class="more">Read more...</span></p>
    </article>
  </section>

  <div class="abs section-title" style="left:80px;top:607px;width:640px">OUR PRODUCTS</div>

  <section class="abs products">
    <article class="product">
      <div class="product-photo photo-prefab" role="img" aria-label="Close-up of red-brown granite pre-fab surface"></div>
      <h3>GRANITE PRE FABS</h3>
      <p>Ready-made pieces cut to standard sizes for quick installs.</p>
    </article>
    <article class="product">
      <div class="product-photo photo-raw" role="img" aria-label="Close-up of cream veined raw granite slab"></div>
      <h3>GRANITE RAW SLABS</h3>
      <p>Full raw slabs direct from the quarry in many finishes.</p>
    </article>
    <article class="product">
      <div class="product-photo photo-tiles" role="img" aria-label="Grid of assorted coloured granite tiles"></div>
      <h3>GRANITE TILES</h3>
      <p>Polished tiles in stock for floors, walls and stairs.</p>
    </article>
  </section>

  <div class="abs gallery-head">
    <div class="section-title">GRANITE TILES</div>
    <div class="gallery-arrows">
      <span><svg width="8" height="8"><path d="M6 1 L2 4 L6 7" fill="none" stroke="#fff" stroke-width="1.5"/></svg></span>
      <span><svg width="8" height="8"><path d="M2 1 L6 4 L2 7" fill="none" stroke="#fff" stroke-width="1.5"/></svg></span>
    </div>
  </div>
  <section class="abs gallery">
    <div class="g1" role="img" aria-label="Red granite tile sample"></div>
    <div class="g2" role="img" aria-label="Beige granite tile sample"></div>
    <div class="g3" role="img" aria-label="Golden brown granite tile sample"></div>
    <div class="g4" role="img" aria-label="Dark grey granite tile sample"></div>
    <div class="g5" role="img" aria-label="White granite tile sample"></div>
    <div class="g6" role="img" aria-label="Light brown granite tile sample"></div>
  </section>

  <footer class="abs footer">
    <div class="footer-col" style="left:0">
      <h4>NAVIGATION</h4>
      <ul><li>Home</li><li>About Us</li><li>Granite Slabs</li><li>Granite Tiles</li><li>Delivery</li><li>Contact Us</li></ul>
    </div>
    <div class="footer-col" style="left:150px">
      <h4>SUPPORT</h4>
      <ul><li>Speak to customer support</li><li>Get in Touch</li><li>Support</li></ul>
    </div>
    <div class="footer-call">
      <div class="phone">CALL US: (555) 284 7730</div>
      <div class="footer-brand"><span class="brand-square"></span><span class="brand-name">SILVER BROOK PETRANO</span></div>
      <address>21 Stone Quarry Road, Granite Park, Porto Verde 40120</address>
    </div>
  </footer>
  <div class="abs copyright">Copyright 2024. All rights reserved.<br>Terms &amp; Conditions | Privacy | Sitemap</div>

</body>
</html>
```